Oak Flooring Brochure (need asap!)

advertising our range of Oak flooring products using exciting photos taken of recent jobs we have completed.
We will use these jobs to showcase our high end LUXURY product aimed at the architectural market.
Main page will feature the current property we are promoting (214c bramford lane) see below:
http://www.homequestlisting.com.au/property-townhouse-vic-tallowmere-548203716

Please use the following photos for the main front of the brochure:

http://files12.listvaultmedia.com.au/images/502846193720558164927305418264/Original27583916.jpg

smaller:
http://files12.listvaultmedia.com.au/images/502846193720558164927305418264/Original27583042.jpg
same size as above?:

http://files12.listvaultmedia.com.au/images/502846193720558164927305418264/Original27583671.jpg

please use my logo that you have from my past project.
my contact number:
0417586294
email:
tedlun@quillbox.net

back side use the following pics:

past projects:
52 Harlow Street

http://files12.listvaultmedia.com.au/images/917254360281947503618294751036/Original26041875.jpg
http://files12.listvaultmedia.com.au/images/917254360281947503618294751036/Original26040932.jpg
And the ones I sent you via email.

*I would like this in a double sided a4*

Text from page:
one version with open for inspection times and auction date (see homequestlisting.com.au link) the other without.

front:

business name. My contact details: Ted Lundqvist Director.

Why us:
We work closely with local estate agents and have intimate knowledge of buyer requirements thus maximising sale price
We offer the most competitive prices

Back:

We specialize in wide engineered timber floors with board widths of 158mm, 189mm, 260mm and can go up to as wide as 410mm.
We create special finishes and colors tailored for the Australian market
We use thick top layers on well-constructed Oak bases to ensure stability and long life unlike others who use multiply.
20mm – multiply construction.
6mm Oak Layer with 14mm base.(use pic as sent to you buy divide the last two layers so that the bottom is 4mm and middle is 1 cm.

benefits of Engineered flooring:
Far greater stability means less floor failures than with solid floors.
Available in a range of pre-finished, hard to achieve colors
Reduced installation time due to pre-finished product.
Can be secret-nailed or just glued down, unlike solid boards which, if over 90mm wide, require top-nailing..

Please note, I require a design sooner rather than later.  thanks!

Please see recent changes to must have's, please use logo's Ive just updated.

Brochure needs to clearly look like we are advertising the Oak flooring.  Invitation/flyer so this must entice people to come and inspect or call for more information.

Consider adding:

Call to action.
"30% off until Christmas!"

"affordable quick way to modernise, update the look and feel of your home!"

FINAL DESIGNS CLOSING IN 24 HOURS, PLEASE SUBMIT FINAL CHANGES.  THANKS

Target Market(s)

architects, developers, mums and dads looking to renovate their homes.

Industry/Entity Type

Advertising

Font styles to use
Other font styles liked:
• GeometricSlab

Requirements
Must have
• our logo, information above
clear uncluttered info
Nice to have
• A similar banner over the main photo on front page of brochure similar to:
http://www.brindleplank.com.au

with the saying

The Architects Choice
Elegant, Leading Edge & Affordable.

use these words below, mix them up, creative jigsaw......

Should not have
• too many colors (white is gold)

```html
<!DOCTYPE html>
<html lang="en">
<head>
<meta charset="utf-8">
<title>Grainhouse Flooring – Engineered Oak Floors</title>
<link href="https://fonts.googleapis.com/css2?family=Roboto+Slab:wght@300;400&family=Arvo:ital@1&display=swap" rel="stylesheet">
<style>
  :root {
    --panel-brown: #a3835f;
    --frame-white: #ffffff;
    --glow-yellow: #f6f1a8;
    --text-white: #ffffff;
    --brand-red: #9a1d3b;
    --band-light: #e9e9e7;
    --band-mid: #d4d4d1;
  }
  * { margin: 0; padding: 0; box-sizing: border-box; }
  html, body { width: 851px; height: 1200px; overflow: hidden; }
  body {
    position: relative;
    background: linear-gradient(90deg, var(--glow-yellow) 0, #fbf9dc 40px, #ffffff 90px);
    font-family: "Roboto Slab", Georgia, serif;
    font-weight: 300;
    color: var(--text-white);
  }
  .top-glow {
    position: absolute; left: 0; top: 0; width: 851px; height: 40px;
    background: linear-gradient(180deg, #f8f4c4, rgba(255,255,255,0));
  }
  .page-frame {
    position: absolute; left: 62px; top: 22px; width: 789px; height: 1010px;
    background: var(--frame-white);
  }
  .content-panel {
    position: absolute; left: 100px; top: 58px; width: 735px; height: 967px;
    background: var(--panel-brown);
  }
  .project-photo, .sample-photo {
    position: absolute;
    border: 4px solid var(--frame-white);
    border-radius: 5px;
    box-shadow: 0 1px 3px rgba(0,0,0,.25);
  }
  .project-photo { left: 20px; width: 281px; height: 189px; }
  .photo-study   { top: 80px;  background: linear-gradient(135deg, #5a5a58 0%, #e8e6e2 45%, #b99c7c 100%); }
  .photo-kitchen { top: 318px; background: linear-gradient(180deg, #e4e0db 0%, #f3f1ee 50%, #a48668 100%); }
  .photo-island  { top: 555px; background: linear-gradient(180deg, #f1efec 0%, #e8e5e1 55%, #9d8064 100%); }
  .photo-living  { top: 797px; background: linear-gradient(180deg, #dedad4 0%, #c8b9a6 55%, #8c7058 100%); }
  .sample-photo {
    left: 393px; top: 450px; width: 341px; height: 229px;
    background: linear-gradient(160deg, #cdb79a 0%, #b99c78 45%, #d4c3a8 75%, #a88a66 100%);
  }
  .copy {
    position: absolute; left: 334px; width: 500px;
    font-size: 17px; line-height: 23px; letter-spacing: .2px;
  }
  .copy p { margin-bottom: 23px; }
  .intro { top: 78px; }
  .benefits { top: 702px; }
  .benefits-title {
    font-family: "Arvo", Georgia, serif; font-style: italic; font-weight: 400;
    font-size: 22px; line-height: 28px; margin-bottom: 22px; margin-left: -16px;
  }
  .benefits p { margin-bottom: 22px; }
  .brand-band {
    position: absolute; left: 0; top: 1025px; width: 851px; height: 175px;
    background: linear-gradient(90deg, var(--band-light), var(--band-mid) 50%, var(--band-light));
  }
  .brand-mark {
    position: absolute; left: 140px; top: 1060px; height: 110px;
    display: flex; align-items: center; gap: 22px;
  }
  .brand-dot { width: 100px; height: 100px; border-radius: 50%; border: 6px solid var(--brand-red); }
  .brand-name {
    font-family: "Roboto Slab", Georgia, serif; font-weight: 400;
    font-size: 44px; color: var(--brand-red); letter-spacing: 1px;
  }
</style>
</head>
<body>
  <div class="top-glow"></div>
  <div class="page-frame"></div>
  <div class="content-panel"></div>

  <div class="project-photo photo-study" role="img" aria-label="Home study with grey wall, white desk and wide oak floor"></div>
  <div class="project-photo photo-kitchen" role="img" aria-label="White kitchen with island bench, open stair and oak floor"></div>
  <div class="project-photo photo-island" role="img" aria-label="Kitchen with marble island and timber-finished wall over oak floor"></div>
  <div class="project-photo photo-living" role="img" aria-label="Open living room with sofa, coffee table and oak floor"></div>
  <div class="sample-photo" role="img" aria-label="Close view of wide limed oak floorboards"></div>

  <section class="copy intro">
    <p>We specialize in wide engineered timber<br>floors with board widths of 158mm, 189mm,<br>260mm and can go up to as wide as 410mm.</p>
    <p>We create special finishes and colors<br>tailored for the Australian market</p>
    <p>We use thick top layers on well-constructed<br>Oak bases to ensure stability and long life unlike<br>others who use multiply.</p>
    <p>20mm – multiply construction.</p>
    <p>6mm Oak Layer with 14mm base. Divide the last two<br>layers so that the bottom is 4mm and middle is 1 cm.</p>
  </section>

  <section class="copy benefits">
    <h2 class="benefits-title">Benefits of Engineered Flooring:</h2>
    <p>Far greater stability means less floor failures than<br>with solid floors.</p>
    <p>Available in a range of pre-finished, hard to achieve<br>&nbsp;colors</p>
    <p>Reduced installation time due to pre-finished product.</p>
    <p>Can be secret-nailed or just glued down,<br>unlike solid boards which, if over 90mm wide, require<br>top-nailing..</p>
  </section>

  <div class="brand-band" role="img" aria-label="Whitewashed timber grain background"></div>
  <div class="brand-mark">
    <span class="brand-dot"></span>
    <span class="brand-name">Grainhouse Flooring</span>
  </div>
</body>
</html>
```